Silver Creek Plumbing Business card & letter head design

We need a new business card and letter head for our plumbing company called silver creek plumbing. attached is the companys logo. We provide domestic and commercial plumbing services in regional western Australia. We are after Something simple yet nice to look at and something that fits within the trade industry.

Target Market(s)

trade/building industry

Contact Information for Business Card

Darl Hensby
Manager
0461 238 574
enquiries@scplumbwork.net.au
ABN: 47 381 905 462
PCL: 5187

Domestic & Commercial Plumbing
Tip Truck & Excavator hire

Colors

Designer to choose colors to be used in the design.

```html
<!DOCTYPE html>
<html lang="en">
<head>
<meta charset="utf-8">
<title>Silver Creek Plumbing – Business Card</title>
<link href="https://fonts.googleapis.com/css2?family=Montserrat:wght@700&family=Roboto:wght@300;400&display=swap" rel="stylesheet">
<style>
  :root {
    --brand-blue: #1356a8;
    --ink-grey: #555a60;
    --band-grey: #58595b;
    --card-white: #ffffff;
    --backdrop: #dcdcdc;
  }
  html, body {
    margin: 0;
    padding: 0;
    width: 1125px;
    height: 1200px;
    overflow: hidden;
    background: var(--backdrop);
  }
  .canvas {
    position: relative;
    width: 1125px;
    height: 1200px;
  }
  .card {
    position: absolute;
    left: 162px;
    width: 800px;
    border-radius: 22px;
    overflow: hidden;
  }
  .card--front {
    top: 100px;
    height: 456px;
    background: var(--card-white);
  }
  .card--back {
    top: 630px;
    height: 458px;
    background: var(--brand-blue);
  }
  .brand-name {
    font-family: "Montserrat", sans-serif;
    font-weight: 700;
    text-transform: uppercase;
    margin: 0;
    line-height: 1.08;
    letter-spacing: 0.5px;
  }
  .card--front .brand-name {
    position: absolute;
    top: 60px;
    right: 57px;
    text-align: right;
    font-size: 38px;
    color: var(--brand-blue);
  }
  .holder-name {
    position: absolute;
    top: 253px;
    left: 57px;
    margin: 0;
    font-family: "Montserrat", sans-serif;
    font-weight: 700;
    font-size: 27px;
    color: var(--brand-blue);
    text-transform: uppercase;
  }
  .holder-role {
    position: absolute;
    top: 288px;
    left: 57px;
    margin: 0;
    font-family: "Roboto", sans-serif;
    font-weight: 400;
    font-size: 20px;
    color: var(--ink-grey);
  }
  .divider {
    position: absolute;
    top: 330px;
    left: 57px;
    width: 686px;
    height: 2px;
    background: var(--ink-grey);
  }
  .contact-list {
    position: absolute;
    top: 354px;
    left: 57px;
    margin: 0;
    padding: 0;
    list-style: none;
    font-family: "Roboto", sans-serif;
    font-weight: 300;
    font-size: 21px;
    color: var(--ink-grey);
  }
  .contact-list li {
    display: flex;
    align-items: center;
    height: 26px;
  }
  .contact-list svg {
    width: 17px;
    height: 17px;
    margin-right: 10px;
    fill: var(--brand-blue);
  }
  .registration {
    position: absolute;
    top: 354px;
    right: 57px;
    margin: 0;
    padding: 0;
    list-style: none;
    font-family: "Roboto", sans-serif;
    font-weight: 300;
    font-size: 21px;
    color: var(--ink-grey);
  }
  .registration li { height: 26px; line-height: 26px; }
  .registration .label { color: var(--brand-blue); }
  .footer-band {
    position: absolute;
    bottom: 0;
    height: 12px;
  }
  .footer-band--grey { left: 0; width: 535px; background: var(--band-grey); }
  .footer-band--blue { left: 545px; right: 0; background: var(--brand-blue); }
  .card--back .brand-name {
    position: absolute;
    top: 150px;
    left: 0;
    right: 0;
    text-align: center;
    font-size: 54px;
    color: var(--card-white);
  }
  .services {
    position: absolute;
    top: 364px;
    left: 0;
    right: 0;
    margin: 0;
    text-align: center;
    font-family: "Roboto", sans-serif;
    font-weight: 300;
    font-size: 23px;
    line-height: 29px;
    color: var(--card-white);
  }
</style>
</head>
<body>
<main class="canvas">
  <section class="card card--front" aria-label="Business card front">
    <h1 class="brand-name">Silver Creek<br>Plumbing</h1>
    <h2 class="holder-name">Darl Hensby</h2>
    <p class="holder-role">Manager</p>
    <div class="divider"></div>
    <ul class="contact-list">
      <li>
        <svg viewBox="0 0 24 24" aria-hidden="true"><path d="M6.6 10.8c1.4 2.8 3.8 5.1 6.6 6.6l2.2-2.2c.3-.3.7-.4 1-.2 1.1.4 2.3.6 3.6.6.6 0 1 .4 1 1V20c0 .6-.4 1-1 1C10.6 21 3 13.4 3 4c0-.6.4-1 1-1h3.5c.6 0 1 .4 1 1 0 1.3.2 2.5.6 3.6.1.3 0 .7-.2 1l-2.3 2.2z"/></svg>
        0461 238 574
      </li>
      <li>
        <svg viewBox="0 0 24 24" aria-hidden="true"><path d="M2 5h20v14H2V5zm2 2v.5l8 5 8-5V7H4zm0 2.8V17h16V9.8l-8 5-8-5z"/></svg>
        enquiries@scplumbwork.net.au
      </li>
    </ul>
    <ul class="registration">
      <li><span class="label">ABN:</span> 47 381 905 462</li>
      <li><span class="label">PCL:</span> 5187</li>
    </ul>
    <div class="footer-band footer-band--grey"></div>
    <div class="footer-band footer-band--blue"></div>
  </section>

  <section class="card card--back" aria-label="Business card back">
    <h1 class="brand-name">Silver Creek<br>Plumbing</h1>
    <p class="services">Domestic &amp; Commercial Plumbing<br>Tip Truck &amp; Excavator hire</p>
  </section>
</main>
</body>
</html>
```